*YO!!! Designers Needed!!* Front Page Cover Needed for a $$Billion Dollar$$ Company

We are a manufacturer of aluminum electrolytic capacitors. We are looking to create a front page cover that will be used on our annual report. We are a publicly listed company and work with many Pinnacle 300 companies, so your work will be viewed by the BIG GUNS and EXECUTIVES around the WORLD! If selected, you may be selected for additional work.

The front page cover should be unique. If elegance, modern, bling, and creativity somehow got together and had a child, that's what the cover page would look like!

Inspired Examples attached. Check them out!

www.velmoro.com

Font styles to use
Sans Serif

Requirements
Must have
• 1. Must include the attached logo. Logo size, color, and placement are at your discretion.

2. Should include the text, '2020 Annual Report'

3. The design should incorporate the use of foil and/or be embossed. The foil can be part of the design or can be the full page. See various examples attached for reference.

4. Shall be in A4 size and vertical orientation.
Nice to have
• Feel free to add any icons or stock photos (for example capacitors or circuit boards) if needed.

Be creative here and don't be afraid to be bold! The end product will be printed and budget is not a limiting factor, so feel free to make it extravagant if needed.

Our slogan is "Think Ahead". This slogan can or cannot be part of the theme.

```html
<!DOCTYPE html>
<html lang="en">
<head>
<meta charset="utf-8">
<title>Velmoro — 2020 Annual Report Cover</title>
<link rel="stylesheet" href="https://fonts.googleapis.com/css2?family=Montserrat:wght@700;800&family=Saira+Condensed:wght@700&family=Josefin+Sans:wght@300&display=swap">
<style>
  :root {
    --paper: #efedea;
    --paper-shade: #e4e2de;
    --copper: #7a3e1b;
    --copper-deep: #5e2f14;
    --ink: #262626;
  }
  html, body {
    margin: 0;
    padding: 0;
    width: 885px;
    height: 1200px;
    overflow: hidden;
    background: var(--paper);
  }
  .cover {
    position: relative;
    width: 885px;
    height: 1200px;
    overflow: hidden;
    background: var(--paper);
  }
  .cover__texture {
    position: absolute;
    inset: 0;
    width: 100%;
    height: 100%;
  }
  .brand-name,
  .slogan,
  .report-year,
  .report-title,
  .website {
    position: absolute;
    margin: 0;
    line-height: 1;
    white-space: nowrap;
  }
  .brand-name {
    left: 40px;
    top: 132px;
    width: 805px;
    font-family: "Montserrat", sans-serif;
    font-weight: 800;
    font-size: 152px;
    letter-spacing: -3px;
    color: var(--copper);
  }
  .slogan {
    right: 52px;
    top: 368px;
    font-family: "Montserrat", sans-serif;
    font-weight: 700;
    font-size: 47px;
    letter-spacing: 0.5px;
    color: var(--copper-deep);
  }
  .report-rule {
    position: absolute;
    left: 40px;
    top: 600px;
    width: 12px;
    height: 436px;
    background: var(--copper);
  }
  .report-year {
    left: 64px;
    top: 584px;
    font-family: "Saira Condensed", sans-serif;
    font-weight: 700;
    font-size: 236px;
    letter-spacing: -2px;
    color: var(--copper);
  }
  .report-title {
    left: 64px;
    font-family: "Montserrat", sans-serif;
    font-weight: 800;
    font-size: 150px;
    letter-spacing: -2px;
    color: var(--copper);
  }
  .report-title--annual { top: 770px; }
  .report-title--report { top: 908px; }
  .website {
    left: 0;
    width: 885px;
    top: 1104px;
    text-align: center;
    font-family: "Josefin Sans", sans-serif;
    font-weight: 300;
    font-size: 22px;
    letter-spacing: 0.45em;
    text-transform: uppercase;
    color: var(--ink);
  }
</style>
</head>
<body>
  <main class="cover">
    <svg class="cover__texture" viewBox="0 0 885 1200" role="img" aria-label="Faint embossed hexagonal circuit-board pattern across the textured paper">
      <defs>
        <radialGradient id="paper-glow" cx="50%" cy="45%" r="75%">
          <stop offset="0" stop-color="#f2f0ed"/>
          <stop offset="1" stop-color="#e6e4e0"/>
        </radialGradient>
      </defs>
      <rect width="885" height="1200" fill="url(#paper-glow)"/>
    </svg>

    <h1 class="brand-name">VELMORO</h1>
    <p class="slogan">THINK AHEAD.</p>

    <div class="report-rule"></div>
    <p class="report-year">2020</p>
    <h2 class="report-title report-title--annual">ANNUAL</h2>
    <h2 class="report-title report-title--report">REPORT</h2>

    <p class="website">www.velmoro.com</p>
  </main>
</body>
</html>
```